Homes, Invest in Non-performing loans

We need only 3 web pages, one for the home, one for the content, one for the properties.
The main focus of our business is to offer non performing loans (before foreclosures) to the general public. All the non-performing mortgages will end in a house, an apartment, a store, etc.
Our customers are able to invest from 10,000usd to 1,000,000usd (average 50,000usd).
Our customers' usual focus groups are employees who want second earnings, perceiving the business feeling without outlay time. They look for a solid finance sense corporation that confers them certainty.
Nearly all our clients desire the house, apartment, store, etc. more than the actual earnings.
The name of our company is BRAMLEY
Reason: We value the time and effort you already invest in our project. We realize that we did't come back on some of the doubts requested by the designers. It will be inequitable to the designers who prerequisite our feedback. We also appreciate the comprehension of the community in this postponement.
Reason: Designers,
We really apreciate all the time and effort you put on our project. From the begining we ask for 3 pages, so now we will leave the 10 finalist and provide some extra time to submit the other 2 pages.
We will race the price in 10%
Target Market(s)
Our customers average investors works as employees and want to have a second income or business without spending time. (People from 35 to 50)
Industry/Entity Type
Finance
Requirements
Should not have
- FLASH

```html
<!DOCTYPE html>
<html lang="en">
<head>
<meta charset="utf-8">
<title>Bramley – Home</title>
<link href="https://fonts.googleapis.com/css2?family=Arimo:wght@400;700&family=Roboto+Condensed:wght@400;700&display=swap" rel="stylesheet">
<style>
:root{
  --blue:#0b3f9c;
  --blue-bright:#2f6fe0;
  --link:#1b4fa8;
  --ink:#333;
  --muted:#888;
  --soft:#b9b9b9;
  --panel-border:#dcdcdc;
  --tint:#f1f1f1;
  --bar:#4a4a4a;
  --page-top:#ffffff;
  --page-bottom:#e9e9e9;
}
*{box-sizing:border-box;margin:0;padding:0}
html,body{width:1200px;height:1062px;overflow:hidden}
body{font-family:"Arimo",Arial,sans-serif;color:var(--ink);background:linear-gradient(var(--page-top) 0,#f1f1f1 420px,var(--page-bottom) 1062px);position:relative}
.abs{position:absolute}
.cond{font-family:"Roboto Condensed","Arial Narrow",sans-serif}

/* header */
.brand{left:322px;top:18px;display:flex;align-items:center;gap:6px}
.brand-name{font-family:"Roboto Condensed",sans-serif;font-weight:700;font-size:22px;color:#333;letter-spacing:.5px}
.brand-mark{width:14px;height:14px;background:#8a8a2a}
.brand-tag{left:323px;top:67px;font-size:4px;letter-spacing:.6px;color:#555}
.nav{top:44px;left:571px;display:flex;gap:44px;font-family:"Roboto Condensed",sans-serif;font-weight:700;font-size:14.5px;color:#222}
.nav .current{color:var(--blue)}
.tagline{right:237px;top:24px;font-family:"Roboto Condensed",sans-serif;font-size:13px;color:var(--link)}

/* hero */
.hero-photo{left:236px;top:88px;width:482px;height:226px;background:linear-gradient(100deg,#b8b9bb 0,#d9d7d2 35%,#7fa4c4 55%,#c9b7a3 75%,#cfcfcf 100%)}
.hero-promo{left:725px;top:88px;width:238px;height:226px;background:var(--blue)}
.promo-title{position:absolute;left:29px;top:56px;font-family:"Roboto Condensed",sans-serif;font-weight:700;font-size:29px;line-height:26px;color:#fff}
.promo-title .accent{color:var(--blue-bright)}
.skip{position:absolute;right:9px;bottom:8px;font-family:"Roboto Condensed",sans-serif;font-size:8px;color:#fff}

.tabs{top:322px;left:236px;display:flex;gap:7px}
.tab{width:238px;height:30px;background:var(--bar);color:#8d8d8d;font-size:7px;font-weight:700;line-height:30px;padding-left:28px;letter-spacing:.3px}

/* panels */
.panel{background:#fff;border:1px solid var(--panel-border)}
.inner{background:var(--tint)}
.welcome{left:236px;top:364px;width:482px;height:182px}
.welcome .inner{position:absolute;left:16px;top:14px;width:451px;height:152px;padding:8px 15px}
.welcome h2{font-size:11px;color:var(--blue);margin-bottom:8px}
.welcome h2 span{color:#aab2c4}
.blurb{font-size:9px;line-height:12px;color:#c2c2c2}
.blurb+.blurb{margin-top:12px}

.finder{left:725px;top:364px;width:238px;height:288px;clip-path:polygon(0 0,100% 0,100% 272px,222px 100%,0 100%)}
.finder .inner{position:absolute;left:16px;top:14px;width:206px;height:258px;padding:7px 5px}
.finder h3{font-size:12px;color:#aab2c4;margin-bottom:6px}
.finder label{display:block;font-size:8.5px;color:#999;margin-top:5px}
.select{width:194px;height:16px;border:1px solid #bbb;background:#fff;font-size:7px;line-height:14px;padding-left:5px;margin-top:3px;position:relative}
.select::after{content:"";position:absolute;right:5px;top:4px;width:4px;height:6px;border-top:2px solid #777;border-bottom:2px solid #777}
.gap{margin-top:9px}
.submit{display:inline-block;margin-top:12px;width:69px;height:18px;background:var(--blue);color:#fff;font-size:6.5px;font-weight:700;text-align:center;line-height:18px;border-radius:2px}
.divider{border-top:1px solid #ddd;margin:13px 0 12px}
.like-head{font-size:11px;font-weight:700;color:var(--blue)}
.like-row{display:flex;gap:3px;margin-top:7px;font-size:7px;align-items:center}
.like-btn{border:1px solid #aaa;background:#fff;padding:2px 4px;display:flex;gap:3px;align-items:center;color:#3b5998}
.like-btn i{width:8px;height:8px;background:#3b5998;display:block}
.like-count{border:1px solid #aaa;background:#fff;padding:2px 3px;color:#555}

.smart{left:236px;top:555px;width:237px;height:220px;clip-path:polygon(0 0,100% 0,100% 204px,221px 100%,0 100%)}
.smart .inner{position:absolute;left:16px;top:14px;width:206px;height:190px;padding:14px 16px}
.smart h2{font-family:"Roboto Condensed",sans-serif;font-weight:700;font-size:21px;line-height:19px;color:var(--blue)}
.smart h2 span{color:#b5b5b5;font-weight:400;display:block}
.smart .blurb{margin-top:12px}
.read{font-size:9px;font-weight:700;color:#6f8fcc;margin-top:5px}

.news{left:481px;top:555px;width:237px;height:307px;clip-path:polygon(0 0,100% 0,100% 291px,221px 100%,0 100%)}
.news .inner{position:absolute;left:16px;top:14px;width:206px;height:289px;padding:16px 15px}
.kicker{font-size:6.5px;color:#888;letter-spacing:.4px}
.story-title{font-size:11px;font-weight:700;line-height:12px;color:#bdbdbd;margin-top:9px}
.story-body{font-size:8px;line-height:12px;color:#c6c6c6;margin-top:4px}
.more{font-size:8.5px;font-weight:700;color:var(--link);margin-top:6px}
.news .rule{border-top:1px solid #ddd;margin:13px 0 10px}
.all-news{position:absolute;right:15px;bottom:18px;font-size:8.5px;font-weight:700;color:var(--link)}

/* footer */
.foot-rule{left:236px;width:727px;border-top:1px solid #d7d7d7}
.sitemap{left:271px;top:910px;display:flex}
.sitemap section{width:102px;font-size:7.5px;line-height:13px;color:#888}
.sitemap h4{font-size:7px;color:#555;font-weight:700;letter-spacing:.3px;margin-bottom:0}
.sitemap p{line-height:10px;margin:1.5px 0}
.legal{left:266px;top:1038px;font-size:6.5px;color:#555;font-weight:700;display:flex;gap:6px}
.legal .copy{color:#c5c5c5;font-weight:400}
.follow{left:828px;top:1036px;display:flex;gap:8px;align-items:center;font-size:7px;color:#999}
.follow i{width:10px;height:10px;background:#999;display:block}
</style>
</head>
<body>

<header>
  <div class="abs brand"><span class="brand-mark"></span><span class="brand-name">BRAMLEY</span></div>
  <div class="abs brand-tag">REMATES HIPOTECARIOS</div>
  <nav class="abs nav"><span class="current">HOME</span><span>CONTENT</span><span>PROPERTY</span></nav>
  <div class="abs tagline">Live Smart</div>
</header>

<div class="abs hero-photo" role="img" aria-label="Photo of a smiling couple preparing vegetables in a modern kitchen"></div>
<div class="abs hero-promo">
  <div class="promo-title"><span class="accent">SMART<br>SOLUTIONS</span><br>FOR ENERGY<br>EFFICIENCY</div>
  <div class="skip">SKIP INTRO</div>
</div>

<div class="abs tabs">
  <div class="tab">INNOVATION IN BRAMLEY »</div>
  <div class="tab">BRAMLEY'S NEWEST COMMUNITY »</div>
  <div class="tab">BRAMLEY'S TOP STORIES »</div>
</div>

<section class="abs panel welcome">
  <div class="inner">
    <h2>Welcome to <span>Bramley Communities.</span></h2>
    <p class="blurb">The gorgeous homes, the smiling neighbors, the shady parks that are just a short stroll away.</p>
    <p class="blurb">These are the places where families put down roots and grow. For more than 30 years, we've been creating true master-planned neighborhoods where everything is thought of – and nothing is overlooked. You'll find us in the best locations throughout the region, the state, the nation – and abroad. We invite you to discover the many reasons why more and more people are choosing to Live Smart in a Bramley community.</p>
  </div>
</section>

<aside class="abs panel finder">
  <div class="inner">
    <h3>Find a Bramley Community</h3>
    <label>Select location:</label><div class="select">All locations</div>
    <label class="gap">Select community:</label><div class="select">All communities</div>
    <label class="gap">Select Price Range:</label><div class="select">From:</div>
    <div class="select" style="margin-top:9px">To:</div>
    <div class="submit">SUBMIT »</div>
    <div class="divider"></div>
    <div class="like-head">Like Us on <span style="color:#777">Circlepage.</span></div>
    <div class="like-row"><span class="like-btn"><i></i>Like</span><span class="like-count">1.5k</span></div>
  </div>
</aside>

<section class="abs panel smart">
  <div class="inner">
    <h2>LIVE SMART<span>THE LATEST<br>WORD</span></h2>
    <p class="blurb">At Bramley Communities, we believe in the concept of living smart. We believe in creating "smart" neighborhoods that have the power to change people's lives in relevant and meaningful ways.</p>
    <p class="read">Read more »</p>
  </div>
</section>

<section class="abs panel news">
  <div class="inner">
    <div class="kicker">LATEST NEWS</div>
    <div class="story-title">Video: Daniel Crane Jr.: We have to grow out this debt crisis</div>
    <div class="story-body">See an insider's endorsement of the housing economy…</div>
    <div class="more">Learn more »</div>
    <div class="rule"></div>
    <div class="story-title">Video: Will Housing Recovery Help Boost Economy?</div>
    <div class="story-body">The Crane Group Chairman Daniel Crane, Jr. on the positive signs for the housing market and economy and their impact on the election. …</div>
    <div class="more">Learn more »</div>
    <div class="rule"></div>
    <div class="all-news">More news »</div>
  </div>
</section>

<footer>
  <div class="abs foot-rule" style="top:896px"></div>
  <div class="abs sitemap">
    <section><h4>ABOUT US</h4><p>Team</p><p>History of Success</p><p>Community<br>Involvement</p><p>Testimonials</p><p>Live Smart Video</p></section>
    <section><h4>COMMUNITIES</h4><p>Cedar Bend Ranch,<br>Wyoming</p><p>Stonebrook, Texas</p><p>Willow Glen, Texas</p><p>Meadow Run, Texas</p><p>Prairie View, Texas</p><p>Oak Hollow, Texas</p></section>
    <section><h4>LAND FOR SALE</h4></section>
    <section><h4>PARTNERS</h4><p>Realtors</p><p>Builder Partners</p><p>Investments</p><p>Public Partnerships</p></section>
    <section><h4>NEWS</h4><p>Newsletters</p><p>Newest Communities</p></section>
    <section><h4>REALTORS</h4></section>
    <section><h4>CONTACT US</h4></section>
  </div>
  <div class="abs foot-rule" style="top:1022px"></div>
  <div class="abs legal"><span class="copy">© BRAMLEY COMMUNITIES · A CRANE COMPANY</span><span>|</span><span>CONTACT US</span><span>|</span><span>PRIVACY POLICY</span><span>|</span><span>BRAMLEY</span></div>
  <div class="abs follow"><span>FOLLOW US:</span><i></i><i></i><i></i></div>
</footer>

</body>
</html>
```